A5 5mm Grid and Dot Grid Page Layout

I need 2 designs:
1] A5 (5.75" x 8" inches final trimmed page size ) 128 journal pages with a 5mm x 5mm grid layout
2} A5 (5.75" x 8" inches final trimmed page size) 128 journal pages with 5mm x 5mm dot grid layout
First and last page should be blank
grid and dot grid should be a light gray color
Final design should you in PDF format

Target Market(s)

Fountain Pen Notebooks

Industry/Entity Type

Notebooks and Journals

Colors

Designer to choose only greyscale colors for use in the design.

Requirements
Must have
• Light gray 5mm x 5mm grid and dot grid page layout. Very thin lines
Should not have
• Thick black grid or dots

```html
<!DOCTYPE html>
<html lang="en">
<head>
<meta charset="utf-8">
<title>A5 Dot Grid and 5mm Grid Journal Pages</title>
<style>
  :root {
    --backdrop: #dadada;
    --paper: #ffffff;
    --dot: #c4c4c4;
    --rule: #e4e4e4;
  }
  html, body {
    margin: 0;
    padding: 0;
    width: 1200px;
    height: 1200px;
    overflow: hidden;
    background: var(--backdrop);
  }
  .spread {
    position: relative;
    width: 1200px;
    height: 1200px;
  }
  .journal-page {
    position: absolute;
    width: 356px;
    height: 504px;
    background: var(--paper);
  }
  .journal-page--dot { left: 190px; top: 350px; }
  .journal-page--grid { left: 658px; top: 348px; }
  .journal-page svg { display: block; width: 100%; height: 100%; }
</style>
</head>
<body>
  <main class="spread">
    <section class="journal-page journal-page--dot" aria-label="A5 dot grid page">
      <svg viewBox="0 0 356 504" xmlns="http://www.w3.org/2000/svg">
        <defs>
          <pattern id="dot-pattern" x="8.7" y="16.8" width="13.21" height="13.21" patternUnits="userSpaceOnUse">
            <circle cx="0.5" cy="0.5" r="0.55" fill="var(--dot)"/>
          </pattern>
        </defs>
        <rect class="dot-field" x="8" y="16" width="340" height="477" fill="url(#dot-pattern)"/>
      </svg>
    </section>

    <section class="journal-page journal-page--grid" aria-label="A5 5mm grid page">
      <svg viewBox="0 0 356 504" xmlns="http://www.w3.org/2000/svg">
        <defs>
          <pattern id="grid-pattern" x="5" y="13" width="11.97" height="11.97" patternUnits="userSpaceOnUse">
            <path d="M 11.97 0 L 0 0 0 11.97" fill="none" stroke="var(--rule)" stroke-width="0.5"/>
          </pattern>
        </defs>
        <rect class="grid-field" x="5" y="13" width="347.1" height="478.8" fill="url(#grid-pattern)"/>
        <rect class="grid-edge" x="5" y="13" width="347.1" height="478.8" fill="none" stroke="var(--rule)" stroke-width="0.5"/>
      </svg>
    </section>
  </main>
</body>
</html>
```